Academic acomlishments and book promotional business card

Must Present my accomplishments in a strong fashion while looking very professional. We will need to make last minute changes in book title in about one to two months so it can't close until then. Must place a great emphasis on peer review. Treat this as if it were my business. It is more important than my titles. Vary fond slightly to emphasize peer review.

Reason: I will need to make small changes in book title in a month or two so it can't close until then.

Target Market(s)

Scholars, employers, patrons, and professionals.

Industry/Entity Type

Business

Contact Information for Business Card

Basic content:

Grant T. Vellimore
Peer review by: Harwick Scholarly Press + Marten Books + R. J. Fallow Co. + Peter Quade & Sons

Evolutionary Scientist + Historian

Academic Consultant, Ellsworth Academic Press

See Overleaf

grantvell@mailbrook.net + Cell. (555) 214-0873

Reverse Side:

In the distant future I see open fields for far more important researches. Psychology will be based on a new foundation, that of the necessary squire Kent of each mental power by gradation. Light will be thrown on the origin of man and his history. --Edmund Farrow [make dash one line]

Book: "Moral Roots or Civic Roots: Adaptive Behaviour,..."

See Friendlane for CV with Endorsements + Writing Sample.

Font styles to use
Serif

Requirements
Must have
• The font has to be big enough etc to be able to use the gold ink at prindo.com, who will print them. Pls see their website for specs.
Nice to have
• Have a capital of the last letter in the Greek alphabet as a decorative element. Though this is not necessary.
Should not have
• Not Ornate or very curvalinear font.

```html
<!DOCTYPE html>
<html lang="en">
<head>
<meta charset="utf-8">
<title>Grant T. Vellimore — Business Card</title>
<link href="https://fonts.googleapis.com/css2?family=Cinzel:wght@400;500;600&display=swap" rel="stylesheet">
<style>
  :root {
    --teal: #0e8a7a;
    --teal-dark: #2c6a60;
    --ink: #3a3a3a;
    --paper: #ffffff;
    --backdrop: #d9d9d9;
  }
  * { box-sizing: border-box; margin: 0; padding: 0; }
  html, body {
    width: 1200px; height: 1000px; overflow: hidden;
    background: var(--backdrop);
    font-family: "Cinzel", "Trajan Pro", serif;
    color: var(--ink);
  }
  .canvas { position: relative; width: 1200px; height: 1000px; }
  .card {
    position: absolute; left: 285px; width: 630px; height: 360px;
    overflow: hidden;
    box-shadow: 0 6px 18px rgba(0,0,0,0.18);
  }

  /* Reverse side */
  .card--reverse { top: 105px; background: var(--teal); }
  .reverse__band {
    position: absolute; left: 0; right: 0; top: 95px; height: 125px;
    background: var(--paper);
    display: flex; align-items: center; justify-content: center;
  }
  .reverse__title {
    font-size: 38px; font-weight: 600; letter-spacing: 1px; color: var(--ink);
    white-space: nowrap;
  }

  /* Front side */
  .card--front { top: 525px; background: var(--paper); }
  .front__name {
    position: absolute; left: 42px; top: 34px;
    font-size: 46px; font-weight: 500; color: var(--teal); letter-spacing: 1px;
    white-space: nowrap;
  }
  .front__peer {
    position: absolute; left: 48px; top: 150px;
    line-height: 1.3;
  }
  .peer__label { margin-bottom: 18px; font-size: 14px; font-weight: 400; }
  .peer__list { list-style: none; font-size: 15px; font-weight: 400; line-height: 1.2; }
  .front__divider {
    position: absolute; left: 340px; top: 125px; width: 2px; height: 170px;
    background: var(--teal);
  }
  .front__details {
    position: absolute; left: 365px; top: 122px;
    font-size: 14px; line-height: 1.25;
  }
  .details__roles { margin-bottom: 14px; }
  .details__contact { list-style: none; margin-top: 14px; }
  .details__contact li {
    display: flex; align-items: center; gap: 10px; margin-bottom: 12px;
    font-size: 14px; white-space: nowrap;
  }
  .details__contact svg { flex: none; }
  .front__stripe { position: absolute; left: 0; bottom: 0; }
</style>
</head>
<body>
<div class="canvas">

  <section class="card card--reverse" aria-label="Card reverse">
    <div class="reverse__band">
      <h2 class="reverse__title">Evolutionary Psychology</h2>
    </div>
  </section>

  <section class="card card--front" aria-label="Card front">
    <h1 class="front__name">Grant T. Vellimore</h1>

    <div class="front__peer">
      <p class="peer__label">Peer review by:</p>
      <ul class="peer__list">
        <li>Harwick Scholarly Press</li>
        <li>Marten Books</li>
        <li>R. J. Fallow Co.</li>
        <li>Peter Quade &amp; Sons</li>
      </ul>
    </div>

    <div class="front__divider"></div>

    <div class="front__details">
      <p class="details__roles">Evolutionary Scientist<br>Historian</p>
      <p class="details__roles">Academic Consultant,<br>Ellsworth Academic Press</p>
      <ul class="details__contact">
        <li>
          <svg width="16" height="14" viewBox="0 0 16 14" aria-hidden="true">
            <path d="M1 4 Q8 -1 15 4 L13 6 L11 4.5 L5 4.5 L3 6 Z" fill="var(--teal)"/>
            <rect x="3" y="7" width="10" height="6" rx="1" fill="var(--teal)"/>
          </svg>
          (555) 214-0873
        </li>
        <li>
          <svg width="16" height="12" viewBox="0 0 16 12" aria-hidden="true">
            <rect x="0.5" y="0.5" width="15" height="11" fill="var(--teal)"/>
            <path d="M1 1 L8 7 L15 1" stroke="#fff" stroke-width="1.2" fill="none"/>
          </svg>
          grantvell@mailbrook.net
        </li>
      </ul>
    </div>

    <svg class="front__stripe" width="630" height="60" viewBox="0 0 630 60" aria-hidden="true">
      <polygon points="0,28 310,28 326,60 0,60" fill="var(--teal)"/>
      <polygon points="318,28 630,0 630,60 334,60" fill="var(--teal-dark)"/>
    </svg>
  </section>

</div>
</body>
</html>
```